Business Card Design for LeafSpire (Farming Devices)

We need Business Cards for our new Company based in Switzerland called "LeafSpire" We develop innovativ products for indoor and outdoor Farming for household and components for vertical farming. Our initial BloomNook gives people the possibility to grow their own food at home all year round. The design should communicate freshness, innovation, health.

```html
<!DOCTYPE html>
<html lang="en">
<head>
<meta charset="utf-8">
<title>LeafSpire Business Card</title>
<link rel="stylesheet" href="https://fonts.googleapis.com/css2?family=Arimo:wght@400;700&display=swap">
<style>
  :root {
    --leaf-green: #76b843;
    --sky-blue: #0f6cbd;
    --card-white: #ffffff;
    --ink: #1e1e1e;
    --backdrop: #c9c9c9;
  }
  * { box-sizing: border-box; margin: 0; padding: 0; }
  html, body { width: 1200px; height: 788px; overflow: hidden; }
  body {
    background: var(--backdrop);
    font-family: "Arimo", Arial, sans-serif;
    position: relative;
  }
  .card {
    position: absolute;
    top: 240px;
    width: 540px;
    height: 308px;
    border-radius: 18px;
    overflow: hidden;
    box-shadow: 0 10px 24px rgba(0,0,0,0.25);
  }
  .card-front { left: 40px; background: var(--card-white); }
  .card-back { left: 620px; background: var(--leaf-green); }

  .front-band { position: absolute; inset: 0; width: 100%; height: 100%; }

  .brand {
    position: absolute;
    display: flex;
    align-items: center;
    gap: 10px;
    font-weight: 700;
    letter-spacing: 0.5px;
  }
  .brand-dot { border-radius: 50%; flex: none; }
  .front-brand { left: 34px; top: 96px; color: var(--leaf-green); font-size: 40px; }
  .front-brand .brand-dot { width: 16px; height: 16px; background: var(--leaf-green); }

  .divider {
    position: absolute;
    left: 262px; top: 78px;
    width: 1px; height: 96px;
    background: var(--sky-blue);
  }

  .contact { position: absolute; left: 286px; top: 44px; color: var(--ink); }
  .person-name { font-size: 22px; font-weight: 700; letter-spacing: 0.5px; line-height: 1; }
  .person-name .first { color: var(--leaf-green); }
  .person-name .last { color: var(--sky-blue); }
  .person-title { font-size: 13px; margin-top: 5px; margin-bottom: 10px; }
  .contact-list { list-style: none; font-size: 13px; line-height: 1.55; }
  .contact-list li { display: flex; align-items: center; gap: 8px; }
  .contact-list svg { width: 11px; height: 11px; flex: none; }

  .address {
    position: absolute;
    left: 200px; bottom: 14px;
    color: var(--card-white);
    font-size: 13px;
    transform: rotate(-8deg);
    transform-origin: left bottom;
  }

  .back-brand {
    left: 0; right: 0; top: 0; bottom: 0;
    justify-content: center;
    color: var(--card-white);
    font-size: 74px;
  }
  .back-brand .brand-dot { width: 26px; height: 26px; background: var(--card-white); }
</style>
</head>
<body>

<section class="card card-front" aria-label="Business card front">
  <svg class="front-band" viewBox="0 0 540 308" preserveAspectRatio="none" aria-hidden="true">
    <path d="M0,308 L0,300 C150,296 330,262 540,196 L540,308 Z" fill="var(--leaf-green)"/>
    <path d="M0,294 C150,290 330,256 540,190" fill="none" stroke="var(--sky-blue)" stroke-width="5"/>
  </svg>

  <div class="brand front-brand"><span class="brand-dot"></span>LeafSpire</div>

  <div class="divider"></div>

  <div class="contact">
    <p class="person-name"><span class="first">DANA</span> <span class="last">WHITFIELD</span></p>
    <p class="person-title">CEO/Founder</p>
    <ul class="contact-list">
      <li>
        <svg viewBox="0 0 12 12"><path d="M2.5 1 L4.5 3.5 L3.5 5 C4.3 6.6 5.4 7.7 7 8.5 L8.5 7.5 L11 9.5 L9.8 11 C5.5 10.6 1.4 6.5 1 2.2 Z" fill="var(--leaf-green)"/></svg>
        555-014-2290
      </li>
      <li>
        <svg viewBox="0 0 12 12"><rect x="0.5" y="2" width="11" height="8" fill="var(--leaf-green)"/><path d="M0.5 2 L6 6.5 L11.5 2" fill="none" stroke="#fff" stroke-width="1.2"/></svg>
        info@leafspire.com
      </li>
      <li>
        <svg viewBox="0 0 12 12"><circle cx="6" cy="6" r="5.3" fill="none" stroke="var(--leaf-green)" stroke-width="1.3"/><ellipse cx="6" cy="6" rx="2.3" ry="5.3" fill="none" stroke="var(--leaf-green)" stroke-width="1"/><path d="M0.7 6 H11.3" stroke="var(--leaf-green)" stroke-width="1"/></svg>
        www.leafspire.com
      </li>
    </ul>
  </div>

  <p class="address">2150 Meadow Lane Country Name, AB 40312</p>
</section>

<section class="card card-back" aria-label="Business card back">
  <div class="brand back-brand"><span class="brand-dot"></span>LeafSpire</div>
</section>

</body>
</html>
```